RTV ELECTRICAL GROUP Website Providing Electrical Services

We're a company providing electrical services to the public. We're located in Bankstown a suburb in Sydney, Australia. We are a team of 4 electricians that provide service work to the public. We work on new construction buildings such as single story, double story & units. We also do office fit outs & commercial factory work.

Target Market(s)

All Age Groups
Construction People
Sydney, Australia

Industry/Entity Type

Electrical

Contact Information for Business Card

Name Gavin Lorrimer
Contact Number 0481 502 743
Company License 904517B
ABN 53 204 871 365
Residential Commercial Industrial
info@rtvelectrical.example.com.au

Coding

Coded - Design and coding required

Number of Pages Required

5+ page

Font styles to use
Serif
Sans Serif

Colors

Designer to choose colors to be used in the design.

Requirements
Must have
• PRESSKIT
• Nice & Simple
• Eye catching
• Easy to Read
• Contact details
• Instagram Linked
• Facebook Page Linked
• All Social Media Linked
• Live Chat
• Form Submission
• Testimonial
• Specify services Offered
• About Us (Company details)
• Industrial Installation Page
• Residential Installation Page
• Commercial Installation Page
• Mode of payment (cash, credit-debit card, cheque)
• Local & national electrical news
• Project Videos
• Newsletter
• Level 2 licensed accredited
• Project pictures and articles
• Awards
• Legalities (company's policy, terms, rules)
• FAQ's (Frequently asked questions)
• Collaboration Projects
• Careers
• Projects
• Suppliers
• Customer Perks (discounts or freebies)
• Employees Informations (pictures and basic information)
• Opening Hours and Map location
• Company Logo & Company License (owner license)
• Accreditation
• Customer Service
• Safety/Safety tips
• Clients information (regular clients)
• Expertise
• Company's processes
• Timeline page
• Homepage
• Specify installations
• Search toolbar
• Portfolio
• Request for an appointment - servicing
• Feedbacks
Nice to have
• Articles (better if recent project articles)
• Advertisement
• Influencer Quote
• Sneak Peeks (if you have new services offered)
• Staff Highlights
• Job Hiring (Career Growth)
• Ratings (Rate our service)
• A day/week in the work
• Personal Anecdotes
• Before and after post projects
• Ecological Values
• Marketing feature
• Tagline
• Streaming interactive videos
• Timeline
• Calendar
• Blog
• Emergency Services/Hotline
• Additional services offered
• Transportation (vehicle - car images of our company)
• Comment box (company - clients)
• Rate Us (Performance rating)
Should not have
• Website shouldn't be dark
• Website shouldn't be hard to read
• Advertisement of competitors
• Moving objects
• Dark background

```html
<!DOCTYPE html>
<html lang="en">
<head>
<meta charset="utf-8">
<title>RTV Electrical Group</title>
<link rel="stylesheet" href="https://fonts.googleapis.com/css2?family=Cabin:wght@400;500;600&family=Open+Sans:wght@400;600;700&family=Poppins:wght@400;500;600&display=swap">
<style>
:root{
  --blue:#1b6196;
  --blue-deep:#174f7c;
  --blue-band:#1e5f92;
  --ink:#111111;
  --text:#555555;
  --muted:#9a9a9a;
  --grey-band:#6a6a6a;
  --footer:#1d1d1d;
  --footer-bar:#141414;
  --footer-text:#8d8d8d;
  --white:#ffffff;
  --line:#e6e6e6;
}
*{margin:0;padding:0;box-sizing:border-box}
html,body{width:1200px;height:3169px;overflow:hidden}
body{position:relative;background:var(--white);font-family:"Open Sans",Arial,sans-serif;color:var(--text)}
.abs{position:absolute}
.photo{position:absolute;overflow:hidden}

/* header */
.site-header{left:0;top:0;width:1200px;height:99px;background:var(--white)}
.brand{left:62px;top:20px;display:flex;align-items:center;gap:10px}
.brand-dot{width:26px;height:26px;border-radius:50%;background:var(--blue)}
.brand-name{font-family:"Cabin",sans-serif;font-size:23px;font-weight:500;color:var(--blue);letter-spacing:.5px}
.main-nav{right:62px;top:34px;display:flex;gap:36px;font-size:15px;font-weight:600;color:var(--ink);text-transform:uppercase}

/* hero */
.hero{left:0;top:99px;width:1200px;height:567px;background:linear-gradient(90deg,#d9dde0 0%,#bcc6cd 30%,#35607e 55%,#1f4a6b 75%,#2f5f80 100%)}
.hero-title{left:420px;top:338px;width:734px;height:131px;background:rgba(22,94,150,.92);color:var(--white);font-family:"Cabin",sans-serif;font-size:46px;line-height:1.05;text-align:right;padding:20px 38px 0 0}

/* welcome */
.feature-photo{top:725px;width:254px;height:215px}
.feature-title{top:968px;font-family:"Poppins",sans-serif;font-size:18px;font-weight:500;color:var(--ink)}
.feature-text{top:1004px;width:250px;font-size:13.5px;line-height:22px;color:var(--text)}
.feature-link{top:1089px;font-size:14px;font-weight:700;color:var(--ink);display:flex;align-items:center;gap:6px}
.welcome-heading{left:647px;top:722px;width:500px;font-family:"Cabin",sans-serif;font-size:38px;line-height:48px;color:var(--ink)}
.welcome-text{left:647px;width:480px;font-size:14px;line-height:25px;color:var(--text)}
.btn{position:absolute;background:var(--blue);color:var(--white);font-size:14px;display:flex;align-items:center;justify-content:center}

/* partner band */
.partner-band{left:0;top:1198px;width:1200px;height:161px;background:var(--grey-band)}
.partner-text{left:62px;top:1230px;font-family:"Cabin",sans-serif;font-size:34px;line-height:40px;color:var(--white)}

/* services */
.services{left:0;top:1359px;width:1200px;height:659px;background:linear-gradient(180deg,#245f90 0%,#1a5b8f 60%,#1b5a8c 100%)}
.services-heading{left:0;top:1428px;width:1200px;text-align:center;font-family:"Cabin",sans-serif;font-size:38px;font-weight:500;color:var(--white)}
.services-sub{left:0;top:1478px;width:1200px;text-align:center;font-size:15px;color:var(--white)}
.service-tile{width:246px;height:182px}
.tile-caption{left:0;bottom:24px;width:246px;height:48px;background:rgba(60,60,60,.85);color:var(--white);font-size:15px;display:flex;align-items:center;justify-content:center}
.tile-search{left:101px;top:40px;width:46px;height:46px;border-radius:50%;background:var(--blue);display:flex;align-items:center;justify-content:center}

/* news */
.news-heading{left:0;top:2080px;width:1200px;text-align:center;font-family:"Cabin",sans-serif;font-size:42px;font-weight:600;color:var(--ink)}
.news-card{top:2183px;width:341px;height:458px;background:var(--white);box-shadow:0 2px 14px rgba(0,0,0,.08)}
.news-card .photo{left:0;top:0;width:341px;height:222px}
.news-tag{background:var(--blue);color:var(--white);font-size:12px;padding:0 12px;height:34px;display:flex;align-items:center;position:absolute}
.news-title{position:absolute;left:20px;font-family:"Poppins",sans-serif;font-size:15.5px;font-weight:600;line-height:26px;color:var(--ink)}
.news-excerpt{position:absolute;left:20px;font-size:13.5px;line-height:22px;color:var(--muted)}
.news-meta{position:absolute;left:20px;font-size:12px;color:#777}
.news-rule{position:absolute;left:20px;height:1px;background:var(--line)}
.news-mini{left:801px;width:340px;height:226px;background:var(--white);box-shadow:0 2px 14px rgba(0,0,0,.08)}

/* footer */
.site-footer{left:0;top:2688px;width:1200px;height:435px;background:var(--footer)}
.footer-brand{left:63px;top:2726px;width:250px;height:65px;background:var(--white);display:flex;align-items:center;gap:8px;padding-left:14px}
.footer-brand .brand-dot{width:20px;height:20px}
.footer-brand .brand-name{font-size:17px}
.footer-about{left:63px;width:260px;font-size:12.5px;line-height:23px;color:var(--footer-text)}
.footer-heading{font-family:"Cabin",sans-serif;font-size:20px;color:#e8e8e8}
.footer-links{left:370px;top:2811px;list-style:none;font-size:13px;color:var(--footer-text)}
.footer-links li{height:33px;display:flex;align-items:center;gap:10px}
.post-thumb{width:64px;height:64px}
.post-title{font-size:13px;line-height:22px;color:var(--footer-text)}
.post-date{font-size:12px;color:#2c7fc1}
.newsletter-text{left:887px;top:2808px;width:260px;font-size:13px;line-height:23px;color:var(--footer-text)}
.email-field{left:887px;top:2876px;width:206px;height:40px;background:#e9e9e9;font-size:12px;color:#888;display:flex;align-items:center;padding-left:12px}
.email-send{left:1093px;top:2876px;width:46px;height:40px;background:var(--blue);display:flex;align-items:center;justify-content:center}
.social{top:3016px;width:36px;height:36px;border-radius:50%;border:1px solid #444}
.footer-bar{left:0;top:3123px;width:1200px;height:46px;background:var(--footer-bar)}
.copyright{left:68px;top:3138px;font-size:12.5px;color:var(--footer-text)}
.bar-nav{right:68px;top:3138px;display:flex;gap:26px;font-size:12.5px;color:var(--footer-text)}
</style>
</head>
<body>

<header class="abs site-header">
  <div class="abs brand"><span class="brand-dot"></span><span class="brand-name">RTV ELECTRICAL GROUP</span></div>
  <nav class="abs main-nav">
    <span>Home</span><span>About</span><span>Services</span><span>Pages</span><span>Our Prices</span><span>FAQ</span><span>Blog</span><span>Contact Us</span>
  </nav>
</header>

<section class="abs hero" role="img" aria-label="Smiling electrician in a hard hat holding a coil of cable in an industrial plant"></section>
<h1 class="abs hero-title">Your vision, Our custom quality<br>Fabrication Services</h1>

<!-- welcome -->
<div class="photo feature-photo" style="left:63px;background:linear-gradient(135deg,#c9a94a,#6e6a5f 50%,#4a4d52)" role="img" aria-label="Electrician in a yellow hard hat working at a switchboard"></div>
<div class="photo feature-photo" style="left:340px;background:linear-gradient(135deg,#e8ecef,#5b84b1 50%,#2d4f7c)" role="img" aria-label="Electrician in a blue cap wiring a panel"></div>
<h3 class="abs feature-title" style="left:63px">Design &amp; Planting</h3>
<h3 class="abs feature-title" style="left:343px">Irrigation and Drainage</h3>
<p class="abs feature-text" style="left:63px">Environmental problems result when exotic plants are placed in the landscape</p>
<p class="abs feature-text" style="left:343px">Environmental problems result when exotic plants are placed in the landscape</p>
<a class="abs feature-link" style="left:65px">Read More <svg width="7" height="9" viewBox="0 0 7 9"><path d="M0 0L7 4.5 0 9z" fill="#111"/></svg></a>
<a class="abs feature-link" style="left:345px">Read More <svg width="7" height="9" viewBox="0 0 7 9"><path d="M0 0L7 4.5 0 9z" fill="#111"/></svg></a>

<h2 class="abs welcome-heading">Welcome to RTV electrical Group</h2>
<p class="abs welcome-text" style="top:854px">We provide ongoing property maintenance which includes lawn mowing, fertilizing, spring and fall cleanups, de-thatching, aerating, seeding, mulching, edging, herbicide application, plant health care, snow plowing, pruning, and tree care and removal.</p>
<p class="abs welcome-text" style="top:976px">We also provide the design and installation of many landscape construction projects including walkways, steps, retaining walls, patios, veneer stone,planting, trans-planting, drainage systems.</p>
<a class="btn" style="left:647px;top:1090px;width:194px;height:49px">Read More</a>

<section class="abs partner-band"></section>
<p class="abs partner-text">We work with our partners to provide project<br>perfetion, join with our parnership.</p>
<a class="btn" style="left:945px;top:1256px;width:196px;height:48px">Learn More</a>

<!-- services -->
<section class="abs services" role="img" aria-label="Faint photo of an electrician under a blue tint"></section>
<h2 class="abs services-heading">Our Services</h2>
<p class="abs services-sub">We provide ongoing property maintenance which includes lawn mowing, fertilizing.</p>

<div class="photo service-tile" style="left:61px;top:1547px;background:linear-gradient(135deg,#e6ebef,#5a7fa8 55%,#2d4a72)" role="img" aria-label="Electrician wiring a switchboard"></div>
<div class="photo service-tile" style="left:338px;top:1547px;background:linear-gradient(135deg,#f1f2f3,#d9dde1 45%,#e07a2a 80%)" role="img" aria-label="Engineer in a hi-vis jacket reading plans">
  <div class="abs tile-search"><svg width="20" height="20" viewBox="0 0 20 20"><circle cx="8" cy="8" r="6" fill="none" stroke="#fff" stroke-width="2.4"/><path d="M12.5 12.5L18 18" stroke="#fff" stroke-width="2.6" stroke-linecap="round"/></svg></div>
  <div class="abs tile-caption">Garden Brick Pathway</div>
</div>
<div class="photo service-tile" style="left:615px;top:1547px;background:linear-gradient(135deg,#c5ad7e,#7a5a3a 45%,#b23a34 80%)" role="img" aria-label="Tool belt with red cable coil"></div>
<div class="photo service-tile" style="left:892px;top:1547px;background:linear-gradient(135deg,#2a3c58,#5e7896 50%,#d7dfe7)" role="img" aria-label="Technician testing a network rack"></div>
<div class="photo service-tile" style="left:61px;top:1760px;background:linear-gradient(135deg,#c5ad7e,#7a5a3a 45%,#b23a34 80%)" role="img" aria-label="Tool belt with red cable coil"></div>
<div class="photo service-tile" style="left:338px;top:1760px;background:linear-gradient(135deg,#2a3c58,#5e7896 50%,#d7dfe7)" role="img" aria-label="Technician testing a network rack"></div>
<div class="photo service-tile" style="left:615px;top:1760px;background:linear-gradient(135deg,#e6ebef,#5a7fa8 55%,#2d4a72)" role="img" aria-label="Electrician wiring a switchboard"></div>
<div class="photo service-tile" style="left:892px;top:1760px;background:linear-gradient(135deg,#f1f2f3,#d9dde1 45%,#e07a2a 80%)" role="img" aria-label="Engineer in a hi-vis jacket reading plans"></div>

<!-- news -->
<h2 class="abs news-heading">Latest News</h2>

<article class="abs news-card" style="left:63px">
  <div class="photo" style="background:linear-gradient(135deg,#c5ad7e,#7a5a3a 45%,#b23a34 80%)" role="img" aria-label="Electrician tool belt with cable coil"></div>
  <h3 class="news-title" style="top:238px">It's Time to Design Your Dream<br>Outdoor Living Space</h3>
  <p class="news-excerpt" style="top:300px;width:300px">How all this mistaken idea of denouncing and praising pain was expound laborious physical except to obtain some advantage...</p>
  <div class="news-rule" style="top:390px;width:300px"></div>
  <p class="news-meta" style="top:410px">July 02, 2017 | 0 Comment</p>
</article>

<article class="abs news-card" style="left:433px">
  <div class="photo" style="background:linear-gradient(135deg,#e6ebef,#5a7fa8 55%,#2d4a72)" role="img" aria-label="Electrician working at a switchboard"></div>
  <span class="news-tag" style="left:10px;top:188px">Blog News</span>
  <h3 class="news-title" style="top:238px">How Landscaping Can Add Curb<br>Appeal to Your Home?</h3>
  <p class="news-excerpt" style="top:300px;width:300px">The great explorer of the truth, master human no rejects or avoids pleasure itself chooses to that has no annoying consequences...</p>
  <div class="news-rule" style="top:390px;width:300px"></div>
  <p class="news-meta" style="top:410px">July 02, 2017 | 0 Comment</p>
</article>

<article class="abs news-mini" style="top:2176px">
  <span class="news-tag" style="left:0;top:0">Blog News</span>
  <h3 class="news-title" style="top:48px">6 Landscaping Methods to Prevent Water<br>Problems</h3>
  <p class="news-excerpt" style="top:116px;width:300px">Must explain to you how all this mistaken idea of pleasure and praisingreat explorer...</p>
  <div class="news-rule" style="top:168px;width:300px"></div>
  <p class="news-meta" style="top:190px">July 02, 2017 | 0 Comment</p>
</article>

<article class="abs news-mini" style="top:2421px">
  <span class="news-tag" style="left:0;top:0">Blog News</span>
  <h3 class="news-title" style="top:48px">We Making Your Perfect Wedding Garden<br>at Home</h3>
  <p class="news-excerpt" style="top:116px;width:300px">Circumstances occur in which toil and all pain can procure him some great pleasure...</p>
  <div class="news-rule" style="top:168px;width:300px"></div>
  <p class="news-meta" style="top:190px">July 02, 2017 | 0 Comment</p>
</article>

<!-- footer -->
<footer class="abs site-footer"></footer>
<div class="abs footer-brand"><span class="brand-dot"></span><span class="brand-name">RTV ELECTRICAL GROUP</span></div>
<p class="abs footer-about" style="top:2808px">We have built an enviable reputation in the consumer goods, heavy industry, high-tech, manufacturing, medical, recreational vehicle, and transportation sectors. multidisciplinary team of engineering experts.</p>
<p class="abs footer-about" style="top:2966px">Our consulting 20 years of experience we'll ensure you always get the best guidance for our customers.</p>

<h4 class="abs footer-heading" style="left:370px;top:2740px">Usefull Links</h4>
<ul class="abs footer-links">
  <li><svg width="6" height="9" viewBox="0 0 6 9"><path d="M1 1l3.5 3.5L1 8" stroke="#8d8d8d" fill="none"/></svg>Business Growth</li>
  <li><svg width="6" height="9" viewBox="0 0 6 9"><path d="M1 1l3.5 3.5L1 8" stroke="#8d8d8d" fill="none"/></svg>Sustainability</li>
  <li><svg width="6" height="9" viewBox="0 0 6 9"><path d="M1 1l3.5 3.5L1 8" stroke="#8d8d8d" fill="none"/></svg>Performance</li>
  <li><svg width="6" height="9" viewBox="0 0 6 9"><path d="M1 1l3.5 3.5L1 8" stroke="#8d8d8d" fill="none"/></svg>Customer Insights</li>
  <li><svg width="6" height="9" viewBox="0 0 6 9"><path d="M1 1l3.5 3.5L1 8" stroke="#8d8d8d" fill="none"/></svg>Organization</li>
  <li><svg width="6" height="9" viewBox="0 0 6 9"><path d="M1 1l3.5 3.5L1 8" stroke="#8d8d8d" fill="none"/></svg>Advanced Analytics</li>
  <li><svg width="6" height="9" viewBox="0 0 6 9"><path d="M1 1l3.5 3.5L1 8" stroke="#8d8d8d" fill="none"/></svg>Free Consultation</li>
</ul>

<h4 class="abs footer-heading" style="left:585px;top:2740px">Latest News</h4>
<div class="photo post-thumb" style="left:587px;top:2812px;background:linear-gradient(135deg,#cfd6dc,#8b98a5)" role="img" aria-label="Desk with laptop and papers"></div>
<div class="abs" style="left:669px;top:2810px;width:180px"><p class="post-title">Create great PressKit theme</p><p class="post-date">July 2015</p></div>
<div class="photo post-thumb" style="left:587px;top:2935px;background:linear-gradient(135deg,#d8dde1,#9aa4ad)" role="img" aria-label="Hands using a tablet"></div>
<div class="abs" style="left:669px;top:2933px;width:180px"><p class="post-title">Retail banks wake up to digital</p><p class="post-date">July 2015</p></div>

<h4 class="abs footer-heading" style="left:887px;top:2745px">Newsletter</h4>
<p class="abs newsletter-text">Sign up today for hints, tips and the latest product news</p>
<div class="abs email-field">Email Address</div>
<div class="abs email-send"><svg width="22" height="16" viewBox="0 0 22 16"><path d="M1 8h18M12 1l7 7-7 7" stroke="#fff" stroke-width="2.4" fill="none"/></svg></div>
<h4 class="abs footer-heading" style="left:887px;top:2950px">Follw Us On</h4>
<span class="abs social" style="left:887px"></span>
<span class="abs social" style="left:933px"></span>
<span class="abs social" style="left:979px"></span>
<span class="abs social" style="left:1025px"></span>

<div class="abs footer-bar"></div>
<p class="abs copyright">Copyrights © 2017 All Rights Reserved</p>
<nav class="abs bar-nav"><span>Home</span><span>About</span><span>Blog</span><span>Contact Us</span><span>FAQ's</span></nav>

</body>
</html>
```